New Custom Pizza Box Design Project For Independant Restaurant

We are looking for creative designs for our new custom printed pizza boxes. Designs should include the following:

-Our logo & company name
-A color scheme similar to our current logo
-Our physical and URL addresses & phone number (menu is attached)
-Ability to scale the design across several box sizes (10x10x2, 14x14x2, 18x13x2,
26x18x2)
- Any creative flair you think will make for the best design

Design can be on a white or kraft (tan) box.
Designs can be either two or three ink colors.

***Please note, designs must be able to be screen printed on boxes***
Updates

Reason: Still debating which to choose

Target Market(s)

Industry/Entity Type

Pizza Delivery

Font styles to use
Other font styles liked:
• Please use font similar to our logo text

Requirements
Must have
• -2 or 3 ink colors
• -company name, address, phone number, URL
• -company logo and colors
• -flexibility to use on different box sizes (10x10x2, 14x14x2, 18x13x2,
• 26x18x2)
• -utilize full printable area on boxes (including 2" dimension on box sides)
• ***Please note, designs must be able to be screen printed on boxes***
Should not have
• Design features with strong similarities to existing designs of other pizzerias

```html
<!DOCTYPE html>
<html lang="en">
<head>
<meta charset="utf-8">
<title>Marco's Larkfield Pizza Box</title>
<link href="https://fonts.googleapis.com/css2?family=Josefin+Sans:wght@300;400;600&family=Ubuntu:wght@400;700&display=swap" rel="stylesheet">
<style>
  :root {
    --box-yellow: #f2b320;
    --box-brown: #6b3a1f;
    --paper: #ecebe7;
    --ink: #262626;
    --sketch-tan: #b5a26a;
    --skyline: #4a4a4a;
    --backdrop: #f4f4f4;
  }
  * { margin: 0; padding: 0; box-sizing: border-box; }
  html, body { width: 1200px; height: 860px; overflow: hidden; background: var(--backdrop); }
  .abs { position: absolute; }

  /* side panels */
  .side {
    position: absolute; background: var(--box-brown); color: var(--box-yellow);
    font-family: "Ubuntu", sans-serif;
  }
  .side-left {
    left: 195px; top: 20px; width: 110px; height: 700px;
    writing-mode: vertical-rl; display: flex; flex-direction: column;
    justify-content: center; padding: 40px 0; gap: 6px; align-items: flex-start;
  }
  .side-bottom {
    left: 305px; top: 720px; width: 700px; height: 110px;
    display: flex; align-items: center; justify-content: space-between; padding: 0 40px;
  }
  .side-tel { font-size: 30px; font-weight: 700; line-height: 1.1; }
  .side-web { font-size: 22px; font-weight: 400; line-height: 1.1; }
  .side-left .side-tel { font-size: 28px; }
  .side-left .side-web { font-size: 20px; }
  .side-brand { font-size: 16px; font-weight: 700; text-transform: uppercase; letter-spacing: 1px; text-align: center; line-height: 1.2; }

  /* lid */
  .lid {
    position: absolute; left: 305px; top: 20px; width: 700px; height: 700px;
    background: var(--box-yellow);
  }
  .paper {
    position: absolute; left: 22px; top: 22px; width: 656px; height: 656px;
    background: linear-gradient(160deg, #f3f2ef 0%, var(--paper) 60%, #dedcd7 100%);
    overflow: hidden; color: var(--ink);
    font-family: "Josefin Sans", sans-serif;
  }
  .headline { left: 18px; top: 30px; font-size: 150px; font-weight: 300; letter-spacing: 8px; line-height: 1; }
  .pizza-art { left: 505px; top: 28px; width: 130px; height: 100px; }
  .tagline-band {
    left: 18px; top: 150px; width: 620px; height: 32px; background: var(--ink);
    color: #fff; font-size: 18px; letter-spacing: 1px; display: flex; align-items: center;
    padding: 4px 14px 0; text-transform: uppercase; white-space: nowrap;
  }
  .tagline-band .since { text-transform: none; border-left: 1px solid #fff; padding-left: 14px; margin-left: auto; }
  .rule-v { width: 1px; background: var(--ink); }
  .rule-h { height: 1px; background: var(--ink); }

  .section-title { left: 18px; top: 255px; font-size: 30px; letter-spacing: 2px; font-weight: 300; white-space: nowrap; }
  .kitchen-art { left: 18px; top: 300px; width: 210px; height: 200px; }
  .web { left: 18px; top: 585px; font-size: 17px; white-space: nowrap; }

  .brand { left: 248px; top: 240px; width: 190px; display: flex; flex-direction: column; align-items: center; gap: 14px; }
  .brand-name {
    font-family: "Ubuntu", sans-serif; font-weight: 700; color: var(--box-brown);
    font-size: 28px; line-height: 1.1; text-align: center; text-transform: uppercase; letter-spacing: 1px;
  }
  .brand-dot { width: 16px; height: 16px; border-radius: 50%; background: var(--box-yellow); }
  .skyline { left: 252px; top: 545px; width: 186px; height: 80px; }

  .oven-art { left: 458px; top: 200px; width: 180px; height: 120px; }
  .story { left: 458px; top: 332px; width: 180px; font-size: 10px; line-height: 1.4; }
  .location { left: 458px; top: 455px; width: 182px; }
  .plaza { font-size: 19px; font-weight: 600; white-space: nowrap; }
  .street { font-size: 13px; font-weight: 600; margin-top: 6px; line-height: 1.3; }
  .tel { font-family: "Ubuntu", sans-serif; font-size: 19px; margin-top: 10px; white-space: nowrap; }
</style>
</head>
<body>
  <aside class="side side-left">
    <div class="side-tel">Tel. 555-014-2290</div>
    <div class="side-web">www.marcoslarkfield.com</div>
  </aside>

  <main class="lid">
    <section class="paper">
      <div class="abs headline">PIZZA</div>
      <svg class="abs pizza-art" role="img" aria-label="Sketched pizza with sliced toppings" viewBox="0 0 130 100">
        <ellipse cx="65" cy="50" rx="63" ry="48" fill="#cfccc4"/>
      </svg>
      <div class="abs tagline-band"><span>The Original Marco's Larkfield</span><span class="since">Since 1985</span></div>

      <div class="abs rule-v" style="left:238px; top:200px; height:440px;"></div>
      <div class="abs rule-v" style="left:448px; top:200px; height:440px;"></div>

      <div class="abs section-title">PIZZA TIME</div>
      <div class="abs rule-h" style="left:18px; top:292px; width:210px;"></div>
      <svg class="abs kitchen-art" role="img" aria-label="Sketch of a pizza maker at a wood oven" viewBox="0 0 210 200">
        <rect width="210" height="200" fill="var(--sketch-tan)"/>
      </svg>
      <div class="abs web">www.marcoslarkfield.com</div>

      <div class="abs brand">
        <div class="brand-name">Marco's<br>Larkfield<br>Pizzeria</div>
        <div class="brand-dot"></div>
      </div>
      <svg class="abs skyline" role="img" aria-label="City skyline silhouette" viewBox="0 0 186 80">
        <rect y="20" width="186" height="60" fill="var(--skyline)" opacity="0.85"/>
      </svg>

      <svg class="abs oven-art" role="img" aria-label="Sketch of a chef beside a brick pizza oven" viewBox="0 0 180 120">
        <rect width="180" height="120" fill="var(--sketch-tan)"/>
      </svg>
      <p class="abs story">Since 1985 the Rossi family has served Millbrook with honest food and friendly service. Known for crisp wings, hand-tossed pies and fresh salads, we make every order to taste. Stop by, call ahead, or order online.</p>
      <div class="abs rule-h" style="left:458px; top:442px; width:182px;"></div>
      <div class="abs location">
        <div class="plaza">Eastbrook Plaza</div>
        <div class="street">1420 Orchard Avenue<br>Millbrook, NY 10999</div>
        <div class="tel">Tel. 555-014-2290</div>
      </div>
    </section>
  </main>

  <aside class="side side-bottom">
    <div>
      <div class="side-tel">Tel. 555-014-2290</div>
      <div class="side-web">www.marcoslarkfield.com</div>
    </div>
    <div class="side-brand">Marco's<br>Larkfield</div>
  </aside>
</body>
</html>
```